Modern Business Card for Industrial Company

We need business cards updated with modern fonts and make it look more technical, sharp and clean. The logo should not be changed, but we are looking for fresh solutions for how other information on the card is laid out in an interesting way. The company provides machinery and services to the ceramic industry and deals with cutting-edge technology. The design should reflect a technologically advanced and modern company that deals with the latest European technologies.

Font styles to use
Sans Serif

Requirements
Must have
• Modern fonts, technical look and feel

```html
<!DOCTYPE html>
<html lang="en">
<head>
<meta charset="utf-8">
<title>Norvan Tech – Business Card</title>
<link rel="stylesheet" href="https://fonts.googleapis.com/css2?family=Montserrat:wght@600&family=Open+Sans:wght@400&display=swap">
<style>
  :root {
    --backdrop: #1f1f1f;
    --brand-red: #b32228;
    --brand-blue: #065592;
    --paper: #ffffff;
    --ink: #4a4a4a;
    --muted: #9a9ea3;
    --rule: #d4d4d4;
  }
  * { margin: 0; padding: 0; box-sizing: border-box; }
  html, body { width: 1200px; height: 1015px; overflow: hidden; background: var(--backdrop); }
  .stage { position: relative; width: 1200px; height: 1015px; }
  .card {
    position: absolute; left: 320px; width: 560px; height: 320px;
    overflow: hidden; background: var(--paper);
  }
  .card--front { top: 157px; }
  .card--back { top: 537px; }

  .front-split { position: absolute; inset: 0; }
  .front-name {
    position: absolute; left: 0; right: 0; top: 122px; text-align: center;
    font-family: "Montserrat", sans-serif; font-weight: 600; font-size: 64px;
    letter-spacing: 6px; color: var(--paper);
  }

  .brand {
    position: absolute; left: 40px; top: 118px; width: 240px;
    display: flex; align-items: center; gap: 10px;
    font-family: "Montserrat", sans-serif; font-weight: 600; font-size: 27px;
    letter-spacing: 2px; color: var(--brand-blue);
  }
  .brand-square { width: 14px; height: 14px; background: var(--brand-blue); flex: none; }

  .divider {
    position: absolute; left: 302px; top: 20px; width: 1px; height: 210px;
    background: linear-gradient(var(--paper), var(--rule) 30%, var(--rule) 70%, var(--paper));
  }

  .contact { position: absolute; left: 325px; top: 46px; font-family: "Open Sans", sans-serif; color: var(--ink); }
  .contact-name {
    font-family: "Montserrat", sans-serif; font-weight: 600; font-size: 17px;
    letter-spacing: 1px; color: var(--brand-blue); text-transform: uppercase;
  }
  .contact-role { font-size: 11px; letter-spacing: 1px; text-transform: uppercase; margin-bottom: 12px; }
  .contact-line {
    display: flex; align-items: center; gap: 7px; font-size: 11px;
    text-transform: uppercase; line-height: 19px; letter-spacing: 0.3px;
  }
  .contact-line svg { width: 11px; height: 11px; flex: none; fill: var(--brand-blue); }
  .contact-line .accent { color: var(--brand-blue); }
  .contact-address { margin-top: 10px; font-size: 11px; text-transform: uppercase; line-height: 16px; letter-spacing: 0.3px; }

  .bands { position: absolute; left: 0; bottom: 0; width: 560px; height: 40px; }
</style>
</head>
<body>
<main class="stage">
  <section class="card card--front">
    <svg class="front-split" viewBox="0 0 560 320" preserveAspectRatio="none" aria-hidden="true">
      <rect width="560" height="320" fill="var(--brand-blue)"/>
      <polygon points="0,0 202,0 392,320 0,320" fill="var(--brand-red)"/>
    </svg>
    <div class="front-name">NORVAN</div>
  </section>

  <section class="card card--back">
    <div class="brand"><span class="brand-square"></span>NORVAN TECH</div>
    <div class="divider"></div>

    <div class="contact">
      <div class="contact-name">Marco Ferretti</div>
      <div class="contact-role">President</div>
      <div class="contact-line">
        <svg viewBox="0 0 24 24"><path d="M6.6 10.8a15.1 15.1 0 0 0 6.6 6.6l2.2-2.2a1 1 0 0 1 1-.25 11.4 11.4 0 0 0 3.6.57 1 1 0 0 1 1 1V20a1 1 0 0 1-1 1A17 17 0 0 1 3 4a1 1 0 0 1 1-1h3.5a1 1 0 0 1 1 1c0 1.25.2 2.45.57 3.57a1 1 0 0 1-.25 1z"/></svg>
        <span>21 555-0192</span>
      </div>
      <div class="contact-line">
        <svg viewBox="0 0 24 24"><path d="M2 5h20v14H2z M2 5l10 8 10-8" fill="var(--brand-blue)" stroke="var(--paper)" stroke-width="1.5"/></svg>
        <span>mferretti@norvantech.com</span>
      </div>
      <div class="contact-line">
        <svg viewBox="0 0 24 24"><circle cx="12" cy="12" r="10"/><path d="M2 12h20M12 2c3 3 3 17 0 20M12 2c-3 3-3 17 0 20" fill="none" stroke="var(--paper)" stroke-width="1.3"/></svg>
        <span>www.<span class="accent">norvantech</span>.com</span>
      </div>
      <div class="contact-address">118 Kiln Avenue, Suite 200<br>Lakemont, GA 30410</div>
    </div>

    <svg class="bands" viewBox="0 0 560 40" aria-hidden="true">
      <polygon points="0,28 330,28 330,40 0,40" fill="var(--brand-blue)"/>
      <polygon points="336,8 560,8 560,40 336,40" fill="var(--brand-red)"/>
    </svg>
  </section>
</main>
</body>
</html>
```